Poultry Animal Health Product Label Design for Backyard Farmers

We need a label design for a new brand (name to be finalized yet - will use ClearHarbor logo attached as a placeholder). We will launch several products for backyard farmers to use on their chickens. These products will treat insect and parasite problems on chickens and their coops. Products will be sold in farm & fleet stores and packaged in a powder bottle (similar to baby powder with shaker top - attached to project with a Tolbrine label on it currently for a different brand/product - should be replaced with proposed design) and aerosol cans. Designs should consider photographic or illustration treatment, incorporation of imagery of farms or chickens, use of bold, bright colors (prefer NOT to use yellow as a competitor brand already uses soft yellow primarily). Design needs to work across 2 different package formats: powder bottle and aerosol.

Product in shaker needs to have this copy on the front (aerosols will be similar in amount and type of copy required - specifics not yet defined):
- ClearHarbor logo
- Poultry Dust
- Controls Northern Fowl Mite, Lice
- Nature-derived active ingredients are safe for use around people and animals
- Ingredients (will be provided for final design, not yet public)

Brainstorming to date that we liked includes landscape imagery, bright/bold images of chickens, potentially more playful integration of chickens (either caricature or photographic with speech bubbles announcing product use like, "Help! I've got mites!"), and potential inclusion of person (should be female or child - could be just arms holding a chicken rather than full body).

Target Market(s)

Consumers with backyard chickens - typically raised as pets for daily eggs

Industry/Entity Type

Health Product

Requirements
Must have
• Design shown as a label on the powder bottle attached
Nice to have
• Extend design to a standard aerosol can to show portfolio look. Does NOT have to be identical across products - could use different chicken images, for instance.
Should not have
• Yellow cannot be the primary or dominant color as several competitors use yellow almost exclusively.

```html
<!DOCTYPE html>
<html lang="en">
<head>
<meta charset="utf-8">
<title>ClearHarbor Poultry Dust Packaging</title>
<link rel="stylesheet" href="https://fonts.googleapis.com/css2?family=Montserrat:wght@600;700&family=Oswald:wght@300;600&family=Roboto+Condensed:ital,wght@0,700;1,700&display=swap">
<style>
  :root {
    --label-red: #dd1f17;
    --label-white: #ffffff;
    --label-edge: #d0d0d0;
    --brand-green: #2a9a3b;
    --ink: #1c1c1c;
    --bubble-grey: #c8c8c8;
    --sky-top: #cfe7f5;
    --sky-low: #eef6f9;
    --hill-green: #6fa43c;
    --field-green: #8bb94a;
    --bottle-light: #ffffff;
    --bottle-shade: #d9d9d9;
    --cap-light: #f4f4f4;
    --cap-shade: #c6c6c6;
    --page: #ffffff;
  }
  html, body {
    margin: 0;
    padding: 0;
    width: 1004px;
    height: 1200px;
    overflow: hidden;
    background: var(--page);
  }
  .canvas {
    position: relative;
    width: 1004px;
    height: 1200px;
  }
  .bottle {
    position: absolute;
    left: 0;
    top: 0;
  }
  .label {
    position: absolute;
    width: 402px;
    height: 955px;
    background: var(--label-white);
    border: 1px solid var(--label-edge);
    border-radius: 22px;
    overflow: hidden;
    box-sizing: border-box;
  }
  .label--flat {
    left: 513px;
    top: 106px;
  }
  .label--on-bottle {
    left: 129px;
    top: 278px;
    transform: scale(0.775);
    transform-origin: top left;
    border-radius: 14px;
  }
  .label__header {
    position: absolute;
    left: 0; top: 0;
    width: 100%;
    height: 132px;
    background: var(--label-red);
    display: flex;
    align-items: center;
    justify-content: center;
  }
  .label__title {
    margin: 0;
    color: var(--label-white);
    font-family: "Montserrat", sans-serif;
    font-weight: 700;
    font-size: 42px;
    letter-spacing: 0.3px;
  }
  .brand-name {
    position: absolute;
    left: 91px;
    top: 478px;
    width: 640px;
    transform: translate(-50%, -50%) rotate(-90deg);
    text-align: center;
    margin: 0;
    color: var(--brand-green);
    font-family: "Montserrat", sans-serif;
    font-weight: 700;
    font-size: 96px;
    line-height: 1;
    white-space: nowrap;
    letter-spacing: -2px;
  }
  .farm-scene {
    position: absolute;
    left: 237px;
    top: 150px;
    width: 165px;
    height: 306px;
    background: linear-gradient(to bottom, var(--sky-top) 0%, var(--sky-low) 55%, var(--hill-green) 72%, var(--field-green) 100%);
  }
  .speech-bubble {
    position: absolute;
    left: 6px;
    top: 4px;
    width: 129px;
    height: 62px;
  }
  .speech-bubble svg {
    position: absolute;
    left: 0; top: 0;
  }
  .speech-bubble__text {
    position: absolute;
    left: 0; top: 8px;
    width: 129px;
    margin: 0;
    text-align: center;
    font-family: "Roboto Condensed", sans-serif;
    font-style: italic;
    font-weight: 700;
    font-size: 17px;
    line-height: 19px;
    color: var(--ink);
  }
  .claim {
    position: absolute;
    right: 31px;
    top: 478px;
    margin: 0;
    text-align: right;
    font-family: "Oswald", sans-serif;
    font-weight: 600;
    font-size: 42px;
    line-height: 48px;
    color: var(--ink);
    text-transform: uppercase;
    letter-spacing: -0.5px;
  }
  .ingredients {
    position: absolute;
    right: 31px;
    top: 690px;
    margin: 0;
    font-family: "Oswald", sans-serif;
    font-weight: 300;
    font-size: 22px;
    color: var(--ink);
  }
  .label__footer {
    position: absolute;
    left: 0; bottom: 0;
    width: 100%;
    height: 145px;
    background: var(--label-red);
    display: flex;
    align-items: center;
    justify-content: center;
  }
  .safety-note {
    margin: 0;
    text-align: center;
    color: var(--label-white);
    font-family: "Roboto Condensed", sans-serif;
    font-weight: 700;
    font-size: 20px;
    line-height: 27px;
  }
</style>
</head>
<body>
<div class="canvas">

  <svg class="bottle" width="1004" height="1200" viewBox="0 0 1004 1200" aria-hidden="true">
    <defs>
      <linearGradient id="bottle-body-shade" x1="0" y1="0" x2="1" y2="0">
        <stop offset="0" stop-color="var(--bottle-shade)"/>
        <stop offset="0.3" stop-color="var(--bottle-light)"/>
        <stop offset="0.7" stop-color="var(--bottle-light)"/>
        <stop offset="1" stop-color="var(--bottle-shade)"/>
      </linearGradient>
      <linearGradient id="bottle-cap-shade" x1="0" y1="0" x2="1" y2="0">
        <stop offset="0" stop-color="var(--cap-shade)"/>
        <stop offset="0.4" stop-color="var(--cap-light)"/>
        <stop offset="1" stop-color="var(--cap-shade)"/>
      </linearGradient>
    </defs>
    <path class="bottle__body"
          d="M165 148 L348 148 C420 175 470 215 478 275 L481 1075 Q481 1114 442 1114 L109 1114 Q70 1114 70 1075 L73 275 C81 215 100 175 165 148 Z"
          fill="url(#bottle-body-shade)" stroke="#cfcfcf" stroke-width="2"/>
    <rect class="bottle__cap" x="173" y="66" width="167" height="86" rx="14"
          fill="url(#bottle-cap-shade)" stroke="#bdbdbd" stroke-width="2"/>
  </svg>

  <div class="label label--on-bottle">
    <header class="label__header">
      <h2 class="label__title">POULTRY DUST</h2>
    </header>
    <p class="brand-name">ClearHarbor</p>
    <div class="farm-scene" role="img" aria-label="Illustration of a white rooster perched on a wooden fence with a red barn and green hills behind">
      <div class="speech-bubble">
        <svg width="129" height="62" viewBox="0 0 129 62" aria-hidden="true">
          <ellipse cx="64" cy="26" rx="62" ry="25" fill="var(--bubble-grey)"/>
          <path d="M38 44 L30 62 L52 48 Z" fill="var(--bubble-grey)"/>
        </svg>
        <p class="speech-bubble__text">Help! I've<br>got mites!</p>
      </div>
    </div>
    <p class="claim">Controls<br>Northern<br>Fowl Mite,<br>Lice</p>
    <p class="ingredients">Ingredients:</p>
    <footer class="label__footer">
      <p class="safety-note">Nature-derived active ingredients<br>are safe for use around people<br>and animals</p>
    </footer>
  </div>

  <div class="label label--flat">
    <header class="label__header">
      <h1 class="label__title">POULTRY DUST</h1>
    </header>
    <p class="brand-name">ClearHarbor</p>
    <div class="farm-scene" role="img" aria-label="Illustration of a white rooster perched on a wooden fence with a red barn and green hills behind">
      <div class="speech-bubble">
        <svg width="129" height="62" viewBox="0 0 129 62" aria-hidden="true">
          <ellipse cx="64" cy="26" rx="62" ry="25" fill="var(--bubble-grey)"/>
          <path d="M38 44 L30 62 L52 48 Z" fill="var(--bubble-grey)"/>
        </svg>
        <p class="speech-bubble__text">Help! I've<br>got mites!</p>
      </div>
    </div>
    <p class="claim">Controls<br>Northern<br>Fowl Mite,<br>Lice</p>
    <p class="ingredients">Ingredients:</p>
    <footer class="label__footer">
      <p class="safety-note">Nature-derived active ingredients<br>are safe for use around people<br>and animals</p>
    </footer>
  </div>

</div>
</body>
</html>
```